Eye Catching Podcast Cover

My Podcast "Velvet Tracks Under Shelves" is a casual, entertaining hangout with friends telling stories, giving valuable advice, and playing great songs that otherwise would still be sitting in a database. It is not just a music podcast which is what I feel the current design communicates.
I engage and lead these artist in conversations about how to pursue any dream. The final design should communicate my unique relationship with singer/songwriters to provide valuable and applicable information on pursing a dream while hearing a uncut or released hit song.
It may just be my picture...??

Target Market(s)

Entrepreneurs, singer/songwriters

Industry/Entity Type

Entertainment

Logo Text

Velvet Tracks Under Shelves

Requirements
Must have
• My picture

```html
<!DOCTYPE html>
<html lang="en">
<head>
<meta charset="utf-8">
<title>Velvet Tracks Under Shelves – Podcast Cover</title>
<link href="https://fonts.googleapis.com/css2?family=Bebas+Neue&display=swap" rel="stylesheet">
<style>
  :root {
    --page-bg: #f2f2f2;
    --teal-deep: #053f44;
    --teal-dark: #0a4f55;
    --teal-band: #1d6661;
    --teal-veil: rgba(120, 170, 168, 0.55);
    --cream: #d5d1aa;
    --white: #ffffff;
    --ink: #0d0d0d;
    --muted: #b9c6c3;
  }
  html, body {
    margin: 0;
    width: 1200px;
    height: 1000px;
    overflow: hidden;
    background: var(--page-bg);
  }
  .podcast-cover {
    position: absolute;
    left: 332px;
    top: 126px;
    width: 568px;
    height: 568px;
  }
  .podcast-cover svg { display: block; }
  .cover-type { font-family: "Bebas Neue", "Oswald", sans-serif; }
  .title-main { fill: var(--white); }
  .title-accent { fill: var(--cream); }
  .title-under { fill: var(--ink); }
  .host-with { fill: var(--muted); }
  .host-name { fill: var(--white); }
  .title-dot { fill: var(--white); }
</style>
</head>
<body>
  <div class="podcast-cover">
    <svg width="568" height="568" viewBox="0 0 568 568" xmlns="http://www.w3.org/2000/svg">
      <defs>
        <linearGradient id="hostPhotoTone" x1="0" y1="0" x2="1" y2="1">
          <stop offset="0" stop-color="#b89a6a"/>
          <stop offset="0.3" stop-color="#d9b48a"/>
          <stop offset="0.55" stop-color="#6b5a4c"/>
          <stop offset="0.8" stop-color="#1a1a1c"/>
          <stop offset="1" stop-color="#111"/>
        </linearGradient>
        <linearGradient id="panelTone" x1="0" y1="0" x2="0" y2="1">
          <stop offset="0" stop-color="#0a4f55"/>
          <stop offset="1" stop-color="#053f44"/>
        </linearGradient>
        <filter id="blockShadow" x="-10%" y="-10%" width="120%" height="130%">
          <feDropShadow dx="-5" dy="5" stdDeviation="0" flood-color="#08261f"/>
        </filter>
        <filter id="softShadow" x="-10%" y="-20%" width="120%" height="140%">
          <feDropShadow dx="-3" dy="3" stdDeviation="0" flood-color="#0b2f2a"/>
        </filter>
      </defs>

      <rect class="host-photo" x="0" y="0" width="568" height="568" fill="url(#hostPhotoTone)"
            role="img" aria-label="Photo of the podcast host smiling, leaning on a table with hands clasped"/>

      <polygon class="title-panel" points="115,0 568,0 568,408 420,452" fill="url(#panelTone)"/>

      <line x1="55" y1="28" x2="535" y2="28" stroke="#0a2e30" stroke-width="1"/>

      <g class="cover-type" filter="url(#blockShadow)">
        <text class="title-main" x="538" y="114" font-size="100" letter-spacing="20" text-anchor="end">VELVET</text>
        <text class="title-accent" x="552" y="244" font-size="132" letter-spacing="2" text-anchor="end">TRACKS</text>
      </g>

      <rect class="title-veil" x="220" y="252" width="348" height="137" fill="var(--teal-veil)"/>

      <g class="cover-type">
        <text class="title-under" x="550" y="306" font-size="66" letter-spacing="14" text-anchor="end">UNDER</text>
      </g>

      <circle class="title-dot" cx="266" cy="346" r="22"/>

      <g class="cover-type" filter="url(#softShadow)">
        <text class="title-main" x="548" y="378" font-size="88" letter-spacing="3" text-anchor="end">SHELVES</text>
      </g>

      <polygon class="host-band" points="0,568 568,400 568,568" fill="var(--teal-band)"/>
      <line x1="290" y1="551" x2="548" y2="484" stroke="#5e958f" stroke-width="1"/>

      <g class="cover-type" transform="translate(190 556) rotate(-15.7)">
        <text class="host-with" x="0" y="0" font-size="24" letter-spacing="3">WITH</text>
        <text class="host-name" x="60" y="0" font-size="38" letter-spacing="4" filter="url(#softShadow)">MARCUS DELANEY</text>
      </g>
    </svg>
  </div>
</body>
</html>
```